KVR Biz Cards

We are a property management company that manages luxury level residential estates. As such, we need a business card design that gives a high end feel. The idea at the moment is to list the services offered on the back of the card, and our company information on the front of the card.

Services for the back of the card are as follows:
Professional Property Management service, Home Hosting & Concierge Service, Holliday Home / Income Property Management

```html
<!DOCTYPE html>
<html lang="en">
<head>
<meta charset="utf-8">
<title>KVR Business Card</title>
<link rel="stylesheet" href="https://fonts.googleapis.com/css2?family=Lato:wght@400;700;900&display=swap">
<style>
  :root {
    --page: #ffffff;
    --card-top: #1c1d1f;
    --card-bottom: #111213;
    --gold: #d9ae35;
    --gold-soft: #c99f30;
    --cream: #ecebdc;
  }
  * { margin: 0; padding: 0; box-sizing: border-box; }
  html, body {
    width: 1200px; height: 1200px; overflow: hidden;
    background: var(--page);
    font-family: "Lato", sans-serif;
  }
  .canvas { position: relative; width: 1200px; height: 1200px; }
  .card {
    position: absolute; left: 222px; width: 755px; height: 432px;
    background: linear-gradient(160deg, var(--card-top), var(--card-bottom));
  }
  .card--front { top: 117px; }
  .card--back { top: 653px; }

  .brand-name {
    position: absolute; color: var(--gold);
    font-family: "Lato", sans-serif; font-weight: 900;
    line-height: 1; letter-spacing: 2px;
  }
  .card--front .brand-name { left: 54px; width: 250px; top: 150px; font-size: 92px; text-align: center; }
  .card--back .brand-name { left: 0; width: 755px; top: 135px; font-size: 60px; text-align: center; }

  .identity { position: absolute; left: 405px; top: 92px; color: var(--cream); }
  .identity__name { font-size: 38px; font-weight: 400; line-height: 1.1; }
  .identity__role { font-size: 22px; font-weight: 400; margin-top: 2px; }

  .contact { position: absolute; left: 405px; top: 183px; list-style: none; color: var(--cream); font-size: 20px; }
  .contact__item { display: flex; align-items: flex-start; height: 32.5px; line-height: 28px; }
  .contact__item--address { line-height: 26px; }
  .contact__icon { width: 16px; height: 16px; margin: 6px 12px 0 3px; flex: none; fill: var(--gold); }

  .services-heading {
    position: absolute; left: 0; width: 755px; top: 244px;
    display: flex; justify-content: center; align-items: center; gap: 36px;
    color: var(--gold); font-size: 19px; font-weight: 700; letter-spacing: 7px;
  }
  .services-heading__rule { width: 60px; height: 2px; background: var(--gold-soft); }
  .services-list {
    position: absolute; left: 0; width: 755px; top: 285px;
    list-style: none; text-align: center; color: var(--gold);
    font-size: 19px; line-height: 28.5px;
  }
</style>
</head>
<body>
<div class="canvas">
  <section class="card card--front">
    <div class="brand-name">KVR</div>
    <div class="identity">
      <p class="identity__name">Your Name Here</p>
      <p class="identity__role">Position</p>
    </div>
    <ul class="contact">
      <li class="contact__item">
        <svg class="contact__icon" viewBox="0 0 16 16"><path d="M3 1.5l3 .5 1 3.5-1.8 1.2c.8 1.9 2 3.2 3.6 4.1L10 9l3.5 1 .5 3-2 1.5C6.5 14 2 9.5 1.5 3.5z"/></svg>
        <span>(123) 000-4567</span>
      </li>
      <li class="contact__item">
        <svg class="contact__icon" viewBox="0 0 16 16"><path d="M1 3h14v1.2L8 9 1 4.2z M1 5.8L8 10.6l7-4.8V13H1z"/></svg>
        <span>your@email.com</span>
      </li>
      <li class="contact__item">
        <svg class="contact__icon" viewBox="0 0 16 16"><circle cx="8" cy="8" r="6.5" fill="none" stroke="#d9ae35" stroke-width="1.5"/><path d="M1.5 8h13M8 1.5c-3 3.5-3 9.5 0 13M8 1.5c3 3.5 3 9.5 0 13M2.5 5h11M2.5 11h11" fill="none" stroke="#d9ae35" stroke-width="1.2"/></svg>
        <span>yourwebsite.com</span>
      </li>
      <li class="contact__item contact__item--address">
        <svg class="contact__icon" viewBox="0 0 16 16"><path d="M8 0.5a5 5 0 0 1 5 5c0 3.5-5 10-5 10S3 9 3 5.5a5 5 0 0 1 5-5zm0 3a2 2 0 1 0 0 4 2 2 0 0 0 0-4z"/></svg>
        <span>123 NW Somewhere St.<br>Somewhere City, 1111</span>
      </li>
    </ul>
  </section>

  <section class="card card--back">
    <div class="brand-name">KVR</div>
    <h2 class="services-heading">
      <span class="services-heading__rule"></span>
      <span>SERVICES</span>
      <span class="services-heading__rule"></span>
    </h2>
    <ul class="services-list">
      <li>Professional Property Management</li>
      <li>Home Hosting and Concierge</li>
      <li>Holliday Home / Income Property Management</li>
    </ul>
  </section>
</div>
</body>
</html>
```